Tri Fold Brochure for Larkmont Financial Planning SA

We need a tri fold and PDF (emailable) brochure for financial planning business located in a rural location in South Australia. I have attached the information we would like included. I would like the brochure to have a blue theme, as this is our corporate colour. I'm looking for something corporate, but not boring. It needs to catch the eye and engage our prospective clients. We have had some structural changes in the business and would like to portray a new company image that means business but is fresh and vibrant, yet very professional. It is possible that we could use the successful bid as a basis for our new website and further stationery needs.

Target Market(s)

Potential financial planning clients. We have a broad market 18-35 wealth accumulators, 35-50 wealth builders, 50-60 Pre-retirement, 60-75 retirement, 75+ Aged Care.

Industry/Entity Type

Financial Planning

Font styles to use
Sans Serif
Other font styles liked:
• Arial, verdana

Colors
0255a3
3176b5
85acd3
cfdeed
eaf1f7
ffffff
33a6d7
0392cd
85cae6

Requirements
Must have
• The Velbrane logo (which is in the uploaded material and cannot be changed), this needs to be placed close to the words as shown in the uploaded material. Our business logo. All the written information that I have attached less any design attributes I have attached. Some relatable photgraphs or images.
Nice to have
• The words "Certainty, Direction, and Peace of Mind" maybe in the back ground somewhere, sort of like a water mark. Any blue scheme is fine, with black and white included, take note of the version of blue in our logo. The fonts I have chosen can be used singularly or in a mixed format.
Should not have
• Photographs or designs used by other financial planning firms. Red, this is too confrontational.

```html
<!DOCTYPE html>
<html lang="en">
<head>
<meta charset="utf-8">
<title>Larkmont Financial Planning SA – Tri Fold Brochure</title>
<link href="https://fonts.googleapis.com/css2?family=Montserrat:wght@300;400;700;800&family=Open+Sans:wght@400;600&display=swap" rel="stylesheet">
<style>
  :root{
    --navy:#0a2f8c;
    --blue:#0255a3;
    --blue-mid:#3176b5;
    --blue-soft:#85acd3;
    --blue-pale:#cfdeed;
    --blue-mist:#eaf1f7;
    --white:#ffffff;
    --ink:#1f2a44;
    --stage:#e4e6ea;
  }
  *{margin:0;padding:0;box-sizing:border-box}
  html,body{width:1200px;height:1200px;overflow:hidden;background:var(--stage)}
  .canvas{position:relative;width:1200px;height:1200px}
  .spread{position:absolute;left:0;top:136px;width:1200px;height:927px;background:var(--white);overflow:hidden;box-shadow:0 10px 30px rgba(0,0,0,.18)}
  .spread-art{position:absolute;inset:0}
  .fold{position:absolute;top:0;bottom:0;width:1px;background:rgba(0,0,0,.06)}
  .fold--one{left:400px}.fold--two{left:800px}

  .panel{position:absolute;top:0;height:927px;width:400px;font-family:"Open Sans",Arial,sans-serif;color:var(--ink)}
  .panel--inside{left:0}
  .panel--contact{left:400px}
  .panel--cover{left:800px}

  .section-title{position:absolute;left:44px;top:58px;color:var(--white);font-family:"Montserrat",Arial,sans-serif;line-height:1}
  .section-title strong{display:block;font-weight:800;font-size:50px}
  .section-title span{display:block;font-weight:300;font-size:58px;margin-top:4px}

  .inside-copy{position:absolute;left:40px;top:272px;width:335px}
  .intro{font-size:13px;line-height:1.35;margin-bottom:14px}
  .copy-heading{font-family:"Montserrat",Arial,sans-serif;font-weight:700;color:var(--blue);font-size:24px;margin-bottom:6px}
  .bullets{list-style:none;font-size:13.5px;line-height:1.35;margin-bottom:16px}
  .bullets li{position:relative;padding-left:14px}
  .bullets li::before{content:"";position:absolute;left:0;top:8px;width:6px;height:6px;border-radius:50%;background:var(--blue)}

  .brand-name{font-family:"Montserrat",Arial,sans-serif;font-weight:400;color:var(--blue);font-size:22px;line-height:1.05}
  .brand--contact{position:absolute;left:44px;top:330px}
  .brand--cover{position:absolute;right:40px;top:36px;text-align:left}

  .contact-list{position:absolute;left:44px;top:440px;list-style:none;font-size:15px;line-height:1.4}
  .contact-list li{display:flex;align-items:flex-start;gap:14px;margin-bottom:6px}
  .contact-list svg{flex:none;width:16px;height:16px;margin-top:3px}

  .tagline{position:absolute;left:40px;top:640px;font-family:"Montserrat",Arial,sans-serif;color:var(--blue)}
  .tagline .strong{font-weight:700;font-size:30px;letter-spacing:-.5px}
  .tagline .light{font-weight:300;font-size:18px;color:#6b7489;line-height:1.3}
  .tagline .line-indent{padding-left:18px}
  .tagline .line-indent2{padding-left:34px}
  .website{position:absolute;left:74px;top:800px;font-size:15px;letter-spacing:3px;color:var(--ink)}
</style>
</head>
<body>
<div class="canvas">
  <div class="spread">
    <svg class="spread-art" viewBox="0 0 1200 927" width="1200" height="927">
      <defs>
        <linearGradient id="photoDesk" x1="0" y1="0" x2="1" y2="1">
          <stop offset="0" stop-color="#f2f6fb"/>
          <stop offset=".5" stop-color="#b8cde4"/>
          <stop offset="1" stop-color="#6f95c2"/>
        </linearGradient>
        <linearGradient id="photoPapers" x1="0" y1="0" x2="0" y2="1">
          <stop offset="0" stop-color="#ffffff" stop-opacity="0"/>
          <stop offset=".4" stop-color="#cfdeed"/>
          <stop offset="1" stop-color="#3f73ad"/>
        </linearGradient>
      </defs>

      <polygon points="0,0 400,0 400,150 0,255" fill="var(--blue)"/>
      <polygon points="250,0 400,0 400,60 300,70" fill="var(--navy)" opacity=".8"/>

      <rect x="0" y="640" width="800" height="287" fill="url(#photoPapers)" role="img" aria-label="Photo: financial statements, charts and a pen on a desk"/>
      <polygon points="0,780 120,780 420,927 240,927 0,850" fill="var(--blue)" opacity=".85"/>
      <polygon points="120,780 200,780 500,927 420,927" fill="var(--navy)" opacity=".9"/>

      <rect x="400" y="520" width="400" height="120" fill="var(--blue-mist)" opacity=".8" role="img" aria-label="Photo: calculator keypad fading into the background"/>
      <polygon points="400,0 520,0 930,380 800,380" fill="var(--blue)"/>
      <polygon points="400,0 440,0 800,330 800,372" fill="var(--navy)"/>

      <polygon points="800,120 1200,120 1200,560 1000,560 800,380" fill="url(#photoDesk)" role="img" aria-label="Photo: hand using a calculator over printed financial charts"/>
      <polygon points="960,150 1110,110 1200,180 1200,260" fill="var(--blue)"/>
      <polygon points="1010,170 1080,150 1200,260 1200,300" fill="var(--navy)" opacity=".85"/>
      <polygon points="800,372 930,380 1070,510 940,510" fill="var(--blue)"/>
    </svg>
    <div class="fold fold--one"></div>
    <div class="fold fold--two"></div>

    <section class="panel panel--inside">
      <h2 class="section-title"><strong>What</strong><span>we do</span></h2>
      <div class="inside-copy">
        <p class="intro">Our Approach is to simplify your financial situation, to make it understandable and manageable over the long term.</p>
        <h3 class="copy-heading">Our Service to You</h3>
        <ul class="bullets">
          <li>Different service packages tailored to your needs</li>
          <li>Options to have fees withdrawn from your investments</li>
          <li>We not only set goals, we monitor and review your investments</li>
          <li>Hourly rate work offered</li>
        </ul>
        <h3 class="copy-heading">We can help you</h3>
        <ul class="bullets">
          <li>Save and accumulate wealth</li>
          <li>Protect your wealth</li>
          <li>Protect your family’s wealth</li>
          <li>Transition from work to retirement</li>
          <li>Maximise your retirement income</li>
          <li>With complex Civicare situations and pension claims</li>
          <li>Manage the cost of Aged Care</li>
        </ul>
      </div>
    </section>

    <section class="panel panel--contact">
      <div class="brand-name brand--contact">Larkmont<br>Financial<br>Planning SA</div>
      <ul class="contact-list">
        <li><svg viewBox="0 0 16 16"><path d="M3 1h3l1 4-2 1c1 2 3 4 5 5l1-2 4 1v3c0 1-1 2-2 2C7 15 1 9 1 3c0-1 1-2 2-2z" fill="var(--blue)"/></svg>08 8000 4172</li>
        <li><svg viewBox="0 0 16 16"><circle cx="8" cy="8" r="6.5" fill="none" stroke="var(--blue)" stroke-width="1.6"/><path d="M1.5 8h13M8 1.5c3 3 3 10 0 13M8 1.5c-3 3-3 10 0 13" fill="none" stroke="var(--blue)" stroke-width="1.2"/></svg>larkmontfpsa.com.au</li>
        <li><svg viewBox="0 0 16 16"><rect x="1" y="3" width="14" height="10" rx="1.5" fill="var(--blue)"/><path d="M1.5 4l6.5 5 6.5-5" fill="none" stroke="var(--white)" stroke-width="1.3"/></svg>office@larkmontfpsa.com.au</li>
        <li><svg viewBox="0 0 16 16"><path d="M8 1a5 5 0 0 1 5 5c0 4-5 9-5 9S3 10 3 6a5 5 0 0 1 5-5z" fill="var(--blue)"/><circle cx="8" cy="6" r="2" fill="var(--white)"/></svg><span>Larkmont Financial Planning SA<br>Level 1 12 Wattle Lane<br>ARDENVALE SA 5399</span></li>
      </ul>
    </section>

    <section class="panel panel--cover">
      <div class="brand-name brand--cover">Larkmont<br>Financial<br>Planning SA</div>
      <div class="tagline">
        <div class="strong">WE PARTNER</div>
        <div class="light line-indent">with our clients to create</div>
        <div class="light line-indent2">A roadmap for their</div>
        <div class="strong line-indent2">FINANCIAL FUTURE</div>
      </div>
      <div class="website">www.larkmontfpsa.com.au</div>
    </section>
  </div>
</div>
</body>
</html>
```